Redesign Website

I currently have a website www.kelvaromotionrx.com that I would like to have redesigned for esthetics and design limitations with the present platform. I will provide my logo, background logo (attached) , current site, foundation grip PSD.zip (attached) and a questionnaire (attached) from a web design company to provide the input to have an impressive site that pleases the eyes and makes an impact. I would also like the site to be mobile friendly.

IMPORTANT:
- The final PSD must include:
o Homepage Mockup
o Internal Pages Mockup
o Mobile site mockup
o Fonts files used in mockup

Final website will be responsive, using the Foundation Framework. Attached you will find a PSD of the Foundation grid – please use this and include with your final PSD. Here is a link for reference:
http://plimtex.com/article/1053/foundation-s-grid-and-photoshop-what-you-

Target Market(s)

Patients for physical therapy

Industry/Entity Type

It Company

Requirements
Must have
• Pages included in the present site. Photos and design should change.
Nice to have
• Should provide information necessary for patients to schedule an appointment
Should not have
• Should not be difficult to read.

```html
<!DOCTYPE html>
<html lang="en">
<head>
<meta charset="utf-8">
<title>Kelvaro Motion & Orthopedic Physical Therapy</title>
<link rel="stylesheet" href="https://fonts.googleapis.com/css2?family=Roboto+Condensed:wght@400;700&family=Roboto+Slab:wght@400&family=Open+Sans:wght@400;600&display=swap">
<style>
:root{
  --red:#a8141a;
  --red-dark:#8c0f14;
  --orange:#e2620f;
  --cream:#f7efe2;
  --card:#efe3c9;
  --text:#3a3a3a;
  --muted:#7a7a7a;
  --yellow:#f2c318;
  --blue:#2a5a96;
  --sky:#2b8fd0;
  --white:#ffffff;
}
*{box-sizing:border-box;margin:0;padding:0}
html,body{width:765px;height:1200px;overflow:hidden}
body{background:var(--cream);font-family:"Open Sans",Arial,sans-serif;color:var(--text);position:relative}
.abs{position:absolute}
.main-nav{left:0;top:0;width:765px;height:30px;background:var(--red);display:flex;gap:15px;padding-left:70px;align-items:center}
.main-nav a{color:var(--white);font:700 11.5px "Roboto Condensed",sans-serif;text-decoration:none}
.site-header{left:0;top:30px;width:765px;height:73px;background:#f9f1e4}
.brand{left:70px;top:37px;width:115px;height:110px;background:var(--white);box-shadow:0 1px 4px rgba(0,0,0,.25);display:flex;flex-direction:column;align-items:center;justify-content:center;gap:6px;text-align:center;z-index:3}
.brand-mark{width:26px;height:26px;border-radius:50%;background:var(--orange)}
.brand-name{font:700 12px "Roboto Condensed",sans-serif;color:var(--red);line-height:1.15;padding:0 6px}
.header-phone{left:280px;top:58px;font:400 19px "Roboto Condensed",sans-serif;color:var(--red);display:flex;align-items:center;gap:4px}
.header-address{left:425px;top:60px;width:110px;font:8.5px/12px "Courier New",monospace;color:#555;white-space:nowrap}
.btn-appt{left:543px;top:57px;width:142px;height:26px;background:var(--orange);color:var(--white);font:700 10.5px "Roboto Condensed",sans-serif;display:flex;align-items:center;justify-content:center;border-radius:2px}
.hero{left:0;top:103px;width:765px;height:292px;background:linear-gradient(90deg,#9fb0b8 0%,#6d7e88 35%,#2a2d30 60%,#1b1b1d 100%)}
.hero-title{left:420px;top:156px;width:300px;font:700 23px/29px "Roboto Condensed",sans-serif;color:var(--white);text-transform:uppercase}
.hero-lead{left:420px;top:252px;width:265px;font:400 11px/16px "Roboto Slab",serif;color:#f2f2f2}
.btn-contact{left:422px;top:313px;width:120px;height:32px;background:var(--orange);color:var(--white);font:700 11px "Roboto Condensed",sans-serif;display:flex;align-items:center;justify-content:center;gap:6px}
.btn-more{left:553px;top:313px;width:108px;height:32px;border:1px solid rgba(255,255,255,.6);color:var(--white);font:700 11px "Roboto Condensed",sans-serif;display:flex;align-items:center;justify-content:center}
.section-title{font:700 19px "Roboto Condensed",sans-serif;color:var(--red);text-transform:uppercase}
.service-card{top:455px;width:197px;height:190px;background:var(--card);border-bottom:3px solid var(--red);padding:7px}
.service-photo{width:100%;height:103px}
.service-list{list-style:none;margin-top:10px}
.service-list li{font-size:9.5px;color:#444;line-height:17px;border-bottom:1px dotted #cbb996;padding-left:10px;position:relative}
.service-list li:last-child{border:none}
.service-list li::before{content:"";position:absolute;left:1px;top:7px;width:4px;height:4px;background:var(--red)}
.contact-title{left:70px;top:678px;font:700 19px "Roboto Condensed",sans-serif;color:var(--red)}
.contact-title span{color:#222}
.contact-copy{left:70px;top:704px;width:405px;font-size:9px;line-height:13px;color:var(--muted)}
.map{left:70px;top:805px;width:405px;height:253px;background:linear-gradient(135deg,#e6e3dc,#d9d6cf)}
.hours{left:490px;top:673px;width:198px;height:142px;background:var(--yellow);padding:10px 12px}
.hours h3{font:700 13px "Roboto Condensed",sans-serif;color:#222;text-align:center;margin-bottom:8px;text-transform:uppercase}
.hours table{width:100%;border-collapse:collapse;font-size:8.5px;color:#333}
.hours td{padding:3.5px 0;border-top:1px solid rgba(0,0,0,.1)}
.hours td:nth-child(2){width:20px}
.doctor{left:490px;top:823px;width:198px;height:132px;background:var(--white);border:1px solid #e2d7c2}
.doctor-photo{left:0;top:0;width:100px;height:105px;background:linear-gradient(180deg,#dfe6ec,#b7c7d6)}
.doctor-name{left:104px;top:20px;font:700 12px/15px "Roboto Condensed",sans-serif;color:var(--red);text-transform:uppercase}
.doctor-sub{left:104px;top:60px;font-size:8.5px;color:#444}
.doctor-call{left:0;bottom:0;width:100%;height:25px;background:var(--red);color:var(--white);font:700 8px "Roboto Condensed",sans-serif;display:flex;align-items:center;justify-content:center;gap:4px}
.doctor-call b{font-size:12px}
.social{left:490px;top:963px;width:198px;height:95px;background:var(--white);border:1px solid #e2d7c2;text-align:center;padding-top:12px}
.social h3{font:700 12.5px "Roboto Condensed",sans-serif;color:var(--red);text-transform:uppercase}
.social p{font-size:8.5px;color:#777;margin-top:2px}
.social-row{display:flex;justify-content:center;gap:6px;margin-top:10px}
.social-btn{width:84px;height:25px;color:var(--white);font:700 9.5px "Roboto Condensed",sans-serif;display:flex;align-items:center;justify-content:center;gap:6px}
.social-btn i{width:12px;height:12px;background:rgba(255,255,255,.85);display:inline-block}
.friendbook{background:var(--blue)}.chirper{background:var(--sky)}
.footer-bar{left:70px;top:1085px;width:618px;height:56px;background:#fbf6ee;border:1px solid #eadfc9}
.footer-brand{left:20px;top:10px;width:40px;text-align:center;font:700 7px "Roboto Condensed",sans-serif;color:var(--red)}
.footer-nav{left:70px;top:14px;display:flex;gap:10px}
.footer-nav a{font:400 9.5px "Roboto Condensed",sans-serif;color:#333;text-decoration:none}
.footer-copy{left:70px;top:32px;font-size:7px;color:#888}
.footer-contact{top:1155px;font-size:9.5px;color:#444;display:flex;align-items:center;gap:5px}
</style>
</head>
<body>
<nav class="main-nav abs">
  <a href="#">Home</a><a href="#">Location</a><a href="#">Hours</a><a href="#">Our Story</a><a href="#">Mission Statement</a><a href="#">Services</a><a href="#">Insurance</a><a href="#">New Patients</a><a href="#">Contact Us</a><a href="#">Testimonials</a><a href="#">Community</a>
</nav>
<header class="site-header abs"></header>
<div class="brand abs"><span class="brand-mark"></span><span class="brand-name">Kelvaro Motion &amp; Orthopedic Physical Therapy</span></div>
<div class="header-phone abs"><svg width="11" height="15" viewBox="0 0 11 15"><path d="M2 1h3l1 4-2 1q1 3 3 5l2-1 2 3-2 2Q3 14 1 4z" fill="#a8141a"/></svg>610-555-0142</div>
<div class="header-address abs">482 ARDWELL AVENUE<br>SUITE 4 TARNFIELD PA</div>
<div class="btn-appt abs">REQUEST AN APPOINTMENT</div>

<section class="hero abs" role="img" aria-label="Therapist treating the ankle of a patient lying on a treatment table"></section>
<h1 class="hero-title abs">KelvaroMotion &amp; Orthopedic Physical Therapy</h1>
<p class="hero-lead abs">15 years of experience and dedication to physical rehabilitation in Ashford County of Dr. Daniel Morvell, PT, DPT, MS.</p>
<div class="btn-contact abs"><svg width="12" height="9" viewBox="0 0 12 9"><rect width="12" height="9" fill="#fff"/><path d="M0 0l6 5 6-5" stroke="#e2620f" fill="none"/></svg>CONTACT US</div>
<div class="btn-more abs">LEARN MORE →</div>

<h2 class="section-title abs" style="left:70px;top:423px">Services We Provide</h2>
<article class="service-card abs" style="left:70px">
  <div class="service-photo" role="img" aria-label="Hands treating a patient's foot" style="background:linear-gradient(135deg,#b4714f,#2a2a2a)"></div>
  <ul class="service-list"><li>Sports Medicine rehabilitation</li><li>Orthopedic Injury rehabilitation</li><li>Post fracture rehabilitation</li></ul>
</article>
<article class="service-card abs" style="left:281px">
  <div class="service-photo" role="img" aria-label="Patient exercising on a treadmill" style="background:linear-gradient(135deg,#2d8f8f,#1e3b3e)"></div>
  <ul class="service-list"><li>Preoperative rehabilitation</li><li>Postoperative rehabilitation</li><li>Spine rehabilitation</li></ul>
</article>
<article class="service-card abs" style="left:491px">
  <div class="service-photo" role="img" aria-label="Therapist using an instrument on a leg" style="background:linear-gradient(135deg,#c99a80,#3a2f2a)"></div>
  <ul class="service-list"><li>Worker's Compensation Injuries</li><li>Work Hardening</li><li>Motor Vehicle Injuries</li></ul>
</article>

<h2 class="contact-title abs">CONTACT US TODAY... <span>(360) 555-0187</span></h2>
<p class="contact-copy abs">Our services are the culmination of 15 years of experience of Dr. Dan Morvell, PT, DPT, MS in the sports and orthopedic physical therapy arena. Dan directed the rehabilitation services for the largest orthopedic group in Ashford County. He has provided the services for an orthopedic and sports medicine group that had specialists in spine, shoulder, elbow, wrist, hand, hip, knee, ankle and foot surgery and treatment. His expertise is the treatment of any and all sports and orthopedic injuries, whether they are the result of trauma, repetitive movements or postures or the result of a surgical intervention.</p>
<div class="map abs" role="img" aria-label="Street map showing the clinic location"></div>

<aside class="hours abs">
  <h3>Our Office Hours</h3>
  <table>
    <tr><td>Monday</td><td>:</td><td>7am-7pm</td></tr>
    <tr><td>Tuesday</td><td>:</td><td>7am-7pm</td></tr>
    <tr><td>Wednesday</td><td>:</td><td>7am-7pm</td></tr>
    <tr><td>Thursday</td><td>:</td><td>7am-2pm</td></tr>
    <tr><td>Friday</td><td>:</td><td>7am-2pm</td></tr>
  </table>
</aside>
<aside class="doctor abs">
  <div class="doctor-photo abs" role="img" aria-label="Portrait of the physical therapist"></div>
  <div class="doctor-name abs">Dan Morvell,<br>PT, DPT, MS</div>
  <div class="doctor-sub abs">Make an appointment</div>
  <div class="doctor-call abs">CALL DAN MORVELL: <b>610-555-0142</b></div>
</aside>
<aside class="social abs">
  <h3>Get Social With Us</h3>
  <p>Connect with us on Friendbook and Chirper</p>
  <div class="social-row"><span class="social-btn friendbook"><i></i>LIKE US</span><span class="social-btn chirper"><i></i>FOLLOW US</span></div>
</aside>

<footer class="footer-bar abs">
  <div class="footer-brand abs">Kelvaro Motion</div>
  <nav class="footer-nav abs"><a href="#">Home</a><a href="#">Location</a><a href="#">Hours</a><a href="#">Our Story</a><a href="#">Mission Statement</a><a href="#">Services</a><a href="#">Insurance</a><a href="#">New Patients</a><a href="#">Contact Us</a><a href="#">Testimonials</a><a href="#">Community</a></nav>
  <div class="footer-copy abs">© Kelvaro Motion &amp; Orthopedic Physical Therapy</div>
</footer>
<div class="footer-contact abs" style="left:70px"><svg width="8" height="11" viewBox="0 0 11 15"><path d="M2 1h3l1 4-2 1q1 3 3 5l2-1 2 3-2 2Q3 14 1 4z" fill="#a8141a"/></svg>Phone: 610-555-0142</div>
<div class="footer-contact abs" style="left:240px"><svg width="10" height="7" viewBox="0 0 12 9"><rect width="12" height="9" fill="#a8141a"/></svg>Email: dmorvell@kelvaromotionrx.com</div>
<div class="footer-contact abs" style="left:466px"><svg width="8" height="11" viewBox="0 0 8 11"><path d="M4 0a4 4 0 0 1 4 4c0 3-4 7-4 7S0 7 0 4a4 4 0 0 1 4-4z" fill="#a8141a"/><circle cx="4" cy="4" r="1.5" fill="#f7efe2"/></svg>Address: 482 Ardwell Avenue Suite 4 Tarnfield PA</div>
</body>
</html>
```